Northfield Builders Guild Business card

We are looking for a new business card design with photo included.
Our business is a nonprofit construction contractor membership organization. We offer business education, assist with business setup and licensing, provide safety training, and provide a member directory.
URL: www.brickwayguildnetwork.org
Color code:
CMYK: 0 cyan, 42 magenta, 100 yellow, 0 black for Print.
Hexidecimal: #FF9900
RGB: R 255; G 153; B 0

```html
<!DOCTYPE html>
<html lang="en">
<head>
<meta charset="utf-8">
<title>Northfield Builders Guild – Business Card</title>
<link rel="stylesheet" href="https://fonts.googleapis.com/css2?family=Montserrat:wght@400;500;700;800;900&display=swap">
<style>
  :root {
    --orange: #ff9900;
    --charcoal: #3a3839;
    --ink: #2e2c2d;
    --paper: #ffffff;
    --backdrop: #e6e6e4;
    --mute: #8d8b8c;
    --photo-sky: #cfdbe6;
    --photo-vest: #e9893f;
  }
  * { box-sizing: border-box; margin: 0; padding: 0; }
  html, body {
    width: 1200px; height: 919px; overflow: hidden;
    background: var(--backdrop);
    font-family: "Montserrat", sans-serif;
  }
  .canvas { position: relative; width: 1200px; height: 919px; }

  .card {
    position: absolute; left: 290px;
    width: 620px; height: 354px;
    background: var(--paper);
    box-shadow: 0 6px 18px rgba(0,0,0,.12);
    overflow: hidden;
  }
  .card--back { top: 70px; }
  .card--front { top: 494px; }

  /* back side */
  .back-panel {
    position: absolute; top: 26px; left: 36px; right: 0; bottom: 30px;
    background: var(--charcoal);
  }
  .back-url {
    position: absolute; left: 14px; bottom: 18px;
    transform-origin: left bottom; transform: rotate(-90deg) translate(0, 100%);
    color: var(--paper); font-size: 15px; font-weight: 400; letter-spacing: .5px;
    white-space: nowrap;
  }
  .services {
    position: absolute; right: 40px; top: 40px;
    list-style: none; text-align: right;
    font-weight: 900; text-transform: uppercase;
    font-size: 23px; line-height: 24px; letter-spacing: 1px;
  }
  .services li { margin-bottom: 16px; }
  .services .light { color: var(--paper); display: block; }
  .services .grey { color: var(--mute); display: block; }

  /* front side */
  .front-photo {
    position: absolute; top: 30px; left: 34px; width: 270px; bottom: 26px;
    background: linear-gradient(160deg, var(--photo-sky) 0%, #b9c8d4 55%, var(--photo-vest) 100%);
  }
  .front-panel {
    position: absolute; top: 0; right: 0; left: 304px; bottom: 26px;
    background: var(--orange);
  }
  .guild-tag {
    position: absolute; left: 58px; bottom: 40px;
    width: 226px; padding: 12px 14px;
    background: var(--charcoal);
    display: flex; align-items: center; gap: 10px;
  }
  .guild-tag__mark { width: 14px; height: 14px; background: var(--orange); flex: none; }
  .guild-tag__name {
    color: var(--paper); font-weight: 800; font-size: 16px; line-height: 19px;
    text-transform: uppercase;
  }
  .contact {
    position: absolute; right: 22px; bottom: 40px; text-align: right; color: var(--ink);
  }
  .contact__name { font-weight: 800; font-size: 34px; letter-spacing: 1px; line-height: 36px; }
  .contact__role { font-weight: 500; font-size: 18px; margin-top: 2px; }
  .contact__rule { width: 110px; height: 2px; background: var(--ink); margin: 10px 0 10px auto; }
  .contact__line { font-size: 15px; font-weight: 500; line-height: 22px; }
  .contact__line strong { font-weight: 700; }
</style>
</head>
<body>
<main class="canvas">

  <section class="card card--back" aria-label="Business card back">
    <div class="back-panel">
      <p class="back-url">www.brickwayguildnetwork.org</p>
      <ul class="services">
        <li><span class="light">Technical</span><span class="grey">Assistance</span></li>
        <li><span class="light">Safety</span><span class="grey">&amp; Compliance</span></li>
        <li><span class="grey">Contractor</span><span class="grey">Directory</span></li>
        <li><span class="grey">Contractor</span><span class="light">Education</span></li>
      </ul>
    </div>
  </section>

  <section class="card card--front" aria-label="Business card front">
    <div class="front-photo" role="img" aria-label="Portrait photo of a contractor in a white hard hat and orange safety vest against the sky"></div>
    <div class="front-panel"></div>
    <div class="guild-tag">
      <span class="guild-tag__mark"></span>
      <span class="guild-tag__name">Northfield Builders Guild</span>
    </div>
    <div class="contact">
      <h1 class="contact__name">DANA HOLLIS</h1>
      <p class="contact__role">construction contractor</p>
      <div class="contact__rule"></div>
      <p class="contact__line">Email; <strong>DanaHollis@nbguild.org</strong></p>
      <p class="contact__line">Call; <strong>(555) 318-2746</strong></p>
    </div>
  </section>

</main>
</body>
</html>
```